Real Estate Sales Brokerage

Design a modern and fresh looking standard size business card, incorporate our logo's color scheme and modern appearance with head shot photo on front side and incorporate our log on the back side

Target Market(s)

Residential Home sales

Industry/Entity Type

Real Estate Agent

Font styles to use
Sans Serif

Colors

Designer to choose colors to be used in the design.

Requirements
Must have
• fresh, modern, not too busy, incorporate head shot in front of the card, incorporate logo in front and back of the card. Use logo design scheme as appropriate.
Nice to have
• horizontal and vertical options to compare would be nice.

```html
<!DOCTYPE html>
<html lang="en">
<head>
<meta charset="utf-8">
<title>Harborview Realty – Business Card</title>
<link href="https://fonts.googleapis.com/css2?family=Open+Sans:ital,wght@0,400;0,600;1,400&display=swap" rel="stylesheet">
<style>
  :root {
    --olive: #6b6a3a;
    --olive-dark: #57562c;
    --gold: #e2c13a;
    --paper: #ffffff;
    --paper-shade: #e9e9e9;
    --ink: #3a3a3a;
    --backdrop: #d9d9d9;
    --photo-suit: #3f5f92;
    --photo-bg: #cfcfcf;
  }
  * { margin: 0; padding: 0; box-sizing: border-box; }
  html, body { width: 1200px; height: 716px; overflow: hidden; }
  body {
    background: var(--backdrop);
    font-family: "Open Sans", sans-serif;
    position: relative;
  }
  .card {
    position: absolute;
    top: 198px;
    width: 540px;
    height: 320px;
    border-radius: 18px;
    overflow: hidden;
    box-shadow: 0 8px 22px rgba(0,0,0,.22);
  }
  /* Back side */
  .card-back {
    left: 40px;
    background: linear-gradient(135deg, #74733f 0%, var(--olive) 55%, var(--olive-dark) 100%);
    color: var(--paper);
  }
  .card-back .brand {
    position: absolute;
    top: 118px; left: 0; right: 0;
    display: flex; align-items: center; justify-content: center; gap: 14px;
  }
  .brand-mark { width: 22px; height: 22px; background: currentColor; }
  .card-back .brand-name {
    font-size: 30px; font-weight: 600; letter-spacing: 1px; text-transform: uppercase;
  }
  .card-back .website {
    position: absolute; top: 178px; left: 0; right: 0;
    text-align: center; font-size: 14px; letter-spacing: .5px;
  }
  /* Front side */
  .card-front {
    left: 620px;
    background: linear-gradient(160deg, var(--paper) 0%, #f4f4f4 60%, var(--paper-shade) 100%);
    color: var(--ink);
  }
  .card-front .brand {
    position: absolute; top: 30px; left: 26px;
    display: flex; align-items: center; gap: 10px;
    color: var(--olive);
  }
  .card-front .brand-mark { width: 16px; height: 16px; }
  .card-front .brand-name {
    font-size: 17px; font-weight: 600; letter-spacing: .8px; text-transform: uppercase;
  }
  .side-strip {
    position: absolute; left: 0; top: 156px; width: 60px; height: 26px;
    background: var(--olive);
    border-top: 3px solid var(--gold);
  }
  .base-rule {
    position: absolute; left: 0; right: 0; top: 254px; height: 3px; background: var(--gold);
  }
  .base-band {
    position: absolute; left: 0; right: 0; top: 262px; height: 38px; background: var(--olive);
  }
  .tagline {
    position: absolute; left: 250px; top: 271px;
    font-size: 13px; font-style: italic; color: var(--paper);
  }
  .headshot {
    position: absolute; left: 22px; top: 92px; width: 205px; height: 208px;
    background: linear-gradient(180deg, var(--photo-bg) 0%, #b9b3ab 45%, var(--photo-suit) 75%, #2f4a78 100%);
  }
  .agent {
    position: absolute; left: 318px; top: 92px;
  }
  .agent-name { font-size: 22px; font-weight: 600; color: #333; line-height: 30px; }
  .agent-title { font-size: 13px; color: var(--olive); line-height: 18px; }
  .contacts {
    position: absolute; left: 318px; top: 148px; list-style: none;
    font-size: 14px; color: #333;
  }
  .contacts li { display: flex; align-items: center; gap: 10px; height: 22px; }
  .contacts svg { width: 13px; height: 13px; fill: var(--gold); flex: none; }
</style>
</head>
<body>
  <section class="card card-back" aria-label="Business card back">
    <div class="brand">
      <span class="brand-mark"></span>
      <span class="brand-name">Harborview Realty</span>
    </div>
    <p class="website">www.yourwebsite.com</p>
  </section>

  <section class="card card-front" aria-label="Business card front">
    <div class="brand">
      <span class="brand-mark"></span>
      <span class="brand-name">Harborview Realty</span>
    </div>

    <div class="side-strip"></div>
    <div class="base-rule"></div>
    <div class="base-band"></div>
    <p class="tagline">Your Tagline Here</p>

    <div class="headshot" role="img" aria-label="Agent headshot photo: man in blue suit and red tie"></div>

    <div class="agent">
      <h1 class="agent-name">Daniel Marsh</h1>
      <p class="agent-title">Job title</p>
    </div>

    <ul class="contacts">
      <li>
        <svg viewBox="0 0 16 16" aria-hidden="true"><path d="M2 5c0-2 2-3 6-3s6 1 6 3v1h-3V5H5v1H2zM4 7h8l2 7H2z"/></svg>
        000 000 0000
      </li>
      <li>
        <svg viewBox="0 0 16 16" aria-hidden="true"><path d="M4 1h8v14H4zM5.5 3v9h5V3z"/></svg>
        000 000 0000
      </li>
      <li>
        <svg viewBox="0 0 16 16" aria-hidden="true"><path d="M1 3h14v10H1zM2 4l6 5 6-5z"/></svg>
        youremail@xyz.com
      </li>
      <li>
        <svg viewBox="0 0 16 16" aria-hidden="true"><path d="M8 1a7 7 0 1 0 0 14A7 7 0 0 0 8 1zm0 1.5c.9 1.2 1.4 2.6 1.5 4.5h-3C6.6 5.1 7.1 3.7 8 2.5zM2.6 7h2.4c.1-1.6.5-3 1.1-4A5.5 5.5 0 0 0 2.6 7zm8.4 0h2.4a5.5 5.5 0 0 0-3.5-4c.6 1 1 2.4 1.1 4zM2.6 9a5.5 5.5 0 0 0 3.5 4c-.6-1-1-2.4-1.1-4zm3.9 0c.1 1.9.6 3.3 1.5 4.5.9-1.2 1.4-2.6 1.5-4.5zm4.5 0c-.1 1.6-.5 3-1.1 4a5.5 5.5 0 0 0 3.5-4z"/></svg>
        www.yourwebsite.com
      </li>
    </ul>
  </section>
</body>
</html>
```